Verpackungsdesign für Lifestyle-Diagnostik und Supplements im Bereich Longevity
Zielgruppe
Wir machen Lifestyle-Diagnostik und Supplements im Bereich Longevity
Aufgabenstellung
Verpackung eines Tests (wie der hier: https://shop.quellmora.com/products/zentrip) in der gezeigten Metallschachtel, Supplements in den gezeigten Dosen. Ein Set besteht aus einem Test und zwei Dosen (morgens und abends). Farbschema und Logo Korunelle wie im Anhang. paar Details zu den Supplements auch in den Dateien
Bitte auch an Prägung und anderen Gestaltungsmöglichkeiten denken

```html
<!DOCTYPE html>
<html lang="de">
<head>
<meta charset="utf-8">
<title>Korunelle – Verpackungsetiketten</title>
<link rel="stylesheet" href="https://fonts.googleapis.com/css2?family=Oswald:wght@500&family=Montserrat:wght@500;700&family=Arimo:wght@400;700&display=swap">
<style>
  :root {
    --teal-dark: #0b4548;
    --teal: #17575a;
    --teal-light: #2a6d70;
    --lime: #9cc23a;
    --lime-pale: #e2edb4;
    --white: #ffffff;
    --stage: #f3f3f1;
    --ink-soft: #dfe9e6;
  }
  * { margin: 0; padding: 0; box-sizing: border-box; }
  html, body { width: 1200px; height: 2257px; overflow: hidden; background: var(--stage); }
  .canvas { position: relative; width: 1200px; height: 2257px; }

  .label {
    position: absolute;
    background: var(--white);
    box-shadow: 0 6px 24px rgba(0,0,0,.12);
    overflow: hidden;
    font-family: "Arimo", Arial, sans-serif;
  }
  .label--am { left: 45px; top: 130px; width: 540px; height: 684px; }
  .label--pm { left: 615px; top: 130px; width: 540px; height: 684px; }
  .label--test { left: 220px; top: 930px; width: 760px; height: 1117px; }

  .brand { position: absolute; left: 0; right: 0; text-align: center; }
  .brand__row { display: inline-flex; align-items: center; gap: 12px; }
  .brand__dot { width: 22px; height: 22px; border-radius: 50%; background: var(--lime); }
  .brand__name {
    font-family: "Montserrat", sans-serif; font-weight: 700;
    color: var(--teal-dark); letter-spacing: .5px;
  }
  .brand__tagline {
    font-family: "Montserrat", sans-serif; font-weight: 500;
    color: var(--lime); letter-spacing: .8px;
  }
  .label--am .brand, .label--pm .brand { top: 78px; }
  .label--am .brand__name, .label--pm .brand__name { font-size: 52px; }
  .label--am .brand__tagline, .label--pm .brand__tagline { font-size: 19px; margin-top: 4px; }

  .timing-band {
    position: absolute; left: 0; right: 0; top: 226px; height: 45px;
    background: linear-gradient(90deg, var(--lime) 0%, var(--lime-pale) 45%, var(--lime-pale) 55%, var(--lime) 100%);
    display: flex; align-items: center; justify-content: center; gap: 8px;
    color: var(--white); font-size: 19px; letter-spacing: .3px;
  }
  .panel {
    position: absolute; left: 0; right: 0; top: 271px; bottom: 0;
    background: var(--teal-dark);
  }
  .formula-title {
    position: absolute; left: 0; right: 0; top: 8px; text-align: center;
    font-family: "Oswald", sans-serif; font-weight: 500; font-size: 108px;
    line-height: 1.1; color: var(--white); letter-spacing: -1px;
  }
  .formula-title__accent { color: var(--lime); }

  .benefits { position: absolute; left: 50px; top: 166px; list-style: none; }
  .benefits li {
    display: flex; align-items: center; gap: 10px;
    color: var(--white); font-size: 14.5px; height: 42px;
  }
  .capsules {
    position: absolute; right: 52px; top: 150px; text-align: center; color: var(--lime);
  }
  .capsules__count { font-family: "Oswald", sans-serif; font-weight: 500; font-size: 86px; line-height: 1; }
  .capsules__unit { color: var(--white); font-weight: 700; font-size: 16px; letter-spacing: 1px; margin-top: 4px; }

  .rule { position: absolute; left: 0; right: 0; height: 5px; background: var(--lime); }
  .label--am .rule, .label--pm .rule { top: 293px; }

  .complex { position: absolute; left: 54px; right: 54px; top: 326px; color: var(--white); }
  .complex__title { font-weight: 700; font-size: 14px; margin-bottom: 10px; }
  .complex__text { font-size: 10.5px; line-height: 1.55; color: var(--ink-soft); }

  /* test box */
  .label--test .brand { top: 262px; }
  .label--test .brand__name { font-size: 74px; }
  .label--test .brand__dot { width: 30px; height: 30px; }
  .label--test .brand__tagline { font-size: 26px; margin-top: 0; }
  .test-kicker {
    position: absolute; left: 0; right: 0; top: 428px; text-align: center;
    font-family: "Oswald", sans-serif; font-weight: 500; font-size: 90px; line-height: 1;
    color: var(--lime);
  }
  .test-header {
    position: absolute; left: 0; right: 0; top: 534px; height: 115px;
    background: var(--teal-dark);
    font-family: "Oswald", sans-serif; font-weight: 500; font-size: 90px;
    color: var(--white); text-align: center; line-height: 115px;
  }
  .label--test .rule { top: 649px; height: 8px; }
  .test-panel {
    position: absolute; left: 0; right: 0; top: 657px; bottom: 0;
    background: linear-gradient(180deg, var(--teal-light) 0%, var(--teal) 40%, var(--teal-dark) 100%);
  }
  .test-claim {
    position: absolute; left: 80px; right: 80px; top: 30px; text-align: center;
    color: var(--white); font-size: 21px; line-height: 1.3;
  }
  .dose {
    position: absolute; left: 167px; width: 422px; height: 80px;
    border: 2px solid var(--lime); border-radius: 40px;
    display: flex; align-items: center; padding-left: 20px; gap: 14px;
  }
  .dose--am { top: 128px; }
  .dose--pm { top: 240px; }
  .dose__icon { width: 40px; height: 40px; border-radius: 50%; background: var(--white);
    display: flex; align-items: center; justify-content: center; }
  .dose__qty { font-family: "Oswald", sans-serif; font-weight: 500; font-size: 62px; color: var(--lime); line-height: 1; }
  .dose__qty span { color: var(--teal-light); font-size: 44px; }
  .dose__text { color: var(--lime); font-size: 23px; line-height: 1.15; }
</style>
</head>
<body>
<main class="canvas">

  <section class="label label--am">
    <div class="brand">
      <div class="brand__row"><span class="brand__dot"></span><span class="brand__name">Korunelle</span></div>
      <div class="brand__tagline">Täglich ein Stück Morgen</div>
    </div>
    <div class="timing-band">
      <svg width="20" height="20" viewBox="0 0 20 20"><circle cx="10" cy="10" r="4.5" fill="#fff"/><g stroke="#fff" stroke-width="1.8" stroke-linecap="round"><line x1="10" y1="1" x2="10" y2="3"/><line x1="10" y1="17" x2="10" y2="19"/><line x1="1" y1="10" x2="3" y2="10"/><line x1="17" y1="10" x2="19" y2="10"/><line x1="3.6" y1="3.6" x2="5" y2="5"/><line x1="15" y1="15" x2="16.4" y2="16.4"/><line x1="3.6" y1="16.4" x2="5" y2="15"/><line x1="15" y1="5" x2="16.4" y2="3.6"/></g></svg>
      Morgens einnehmen
    </div>
    <div class="panel">
      <h1 class="formula-title"><span class="formula-title__accent">AM</span> FORMEL</h1>
      <ul class="benefits">
        <li><svg width="24" height="24" viewBox="0 0 24 24"><circle cx="12" cy="12" r="11" fill="#9cc23a"/><path d="M6.5 12.5l3.5 3.5 7.5-8" stroke="#fff" stroke-width="2.4" fill="none" stroke-linecap="round" stroke-linejoin="round"/></svg>Unterstützt die Tagesenergie</li>
        <li><svg width="24" height="24" viewBox="0 0 24 24"><circle cx="12" cy="12" r="11" fill="#9cc23a"/><path d="M6.5 12.5l3.5 3.5 7.5-8" stroke="#fff" stroke-width="2.4" fill="none" stroke-linecap="round" stroke-linejoin="round"/></svg>Mitochondriale Aktivierung</li>
        <li><svg width="24" height="24" viewBox="0 0 24 24"><circle cx="12" cy="12" r="11" fill="#9cc23a"/><path d="M6.5 12.5l3.5 3.5 7.5-8" stroke="#fff" stroke-width="2.4" fill="none" stroke-linecap="round" stroke-linejoin="round"/></svg>Hilft, biologische Rhythmen zu regulieren</li>
      </ul>
      <div class="capsules"><div class="capsules__count">30</div><div class="capsules__unit">KAPSELN</div></div>
      <div class="rule"></div>
      <div class="complex">
        <div class="complex__title">Morgen-Nährstoffkomplex</div>
        <p class="complex__text">Formuliert zur Unterstützung der zellulären Energieproduktion und zur<br>Förderung optimaler Morgenenergie.</p>
      </div>
    </div>
  </section>

  <section class="label label--pm">
    <div class="brand">
      <div class="brand__row"><span class="brand__dot"></span><span class="brand__name">Korunelle</span></div>
      <div class="brand__tagline">Täglich ein Stück Morgen</div>
    </div>
    <div class="timing-band">
      <svg width="20" height="20" viewBox="0 0 20 20"><path d="M12 2a8 8 0 1 0 6 13A7 7 0 0 1 12 2z" fill="#fff"/></svg>
      Abends einnehmen
    </div>
    <div class="panel">
      <h1 class="formula-title"><span class="formula-title__accent">PM</span> FORMEL</h1>
      <ul class="benefits">
        <li><svg width="24" height="24" viewBox="0 0 24 24"><circle cx="12" cy="12" r="11" fill="#9cc23a"/><path d="M6.5 12.5l3.5 3.5 7.5-8" stroke="#fff" stroke-width="2.4" fill="none" stroke-linecap="round" stroke-linejoin="round"/></svg>Unterstützt die nächtliche Regeneration</li>
        <li><svg width="24" height="24" viewBox="0 0 24 24"><circle cx="12" cy="12" r="11" fill="#9cc23a"/><path d="M6.5 12.5l3.5 3.5 7.5-8" stroke="#fff" stroke-width="2.4" fill="none" stroke-linecap="round" stroke-linejoin="round"/></svg>Reduziert oxidativen Stress</li>
        <li><svg width="24" height="24" viewBox="0 0 24 24"><circle cx="12" cy="12" r="11" fill="#9cc23a"/><path d="M6.5 12.5l3.5 3.5 7.5-8" stroke="#fff" stroke-width="2.4" fill="none" stroke-linecap="round" stroke-linejoin="round"/></svg>Fördert tiefe Erholung</li>
      </ul>
      <div class="capsules"><div class="capsules__count">30</div><div class="capsules__unit">KAPSELN</div></div>
      <div class="rule"></div>
      <div class="complex">
        <div class="complex__title">Abend-Nährstoffkomplex</div>
        <p class="complex__text">Formuliert zur Unterstützung tiefer nächtlicher Reparaturprozesse und zur<br>Förderung gesunder Zellregeneration.</p>
      </div>
    </div>
  </section>

  <section class="label label--test">
    <div class="brand">
      <div class="brand__row"><span class="brand__dot"></span><span class="brand__name">Korunelle</span></div>
      <div class="brand__tagline">Täglich ein Stück Morgen</div>
    </div>
    <div class="test-kicker">LANGLEBIGKEITS</div>
    <div class="test-header">DIAGNOSETEST</div>
    <div class="rule"></div>
    <div class="test-panel">
      <p class="test-claim">Messen, was wirklich zählt. Verstehen Sie Ihr<br>biologisches Alter.</p>
      <div class="dose dose--am">
        <span class="dose__icon"><svg width="26" height="26" viewBox="0 0 20 20"><circle cx="10" cy="10" r="4.5" fill="#0b4548"/><g stroke="#0b4548" stroke-width="1.8" stroke-linecap="round"><line x1="10" y1="1" x2="10" y2="3"/><line x1="10" y1="17" x2="10" y2="19"/><line x1="1" y1="10" x2="3" y2="10"/><line x1="17" y1="10" x2="19" y2="10"/><line x1="3.6" y1="3.6" x2="5" y2="5"/><line x1="15" y1="15" x2="16.4" y2="16.4"/><line x1="3.6" y1="16.4" x2="5" y2="15"/><line x1="15" y1="5" x2="16.4" y2="3.6"/></g></svg></span>
        <span class="dose__qty">1<span>X</span></span>
        <span class="dose__text">Morning<br>Supplement-Dose</span>
      </div>
      <div class="dose dose--pm">
        <span class="dose__icon"><svg width="26" height="26" viewBox="0 0 20 20"><path d="M12 2a8 8 0 1 0 6 13A7 7 0 0 1 12 2z" fill="#0b4548"/></svg></span>
        <span class="dose__qty">1<span>X</span></span>
        <span class="dose__text">Evening<br>Supplement-Dose</span>
      </div>
    </div>
  </section>

</main>
</body>
</html>
```